Medical VIP club - small design

Please read the specs in a design brief attached. Also we don't have logo in a Vector format and attaching the only version we have.

Industry/Entity Type

Club

```html
<!DOCTYPE html>
<html lang="en">
<head>
<meta charset="utf-8">
<title>Medvista – VIP Medical Club</title>
<link rel="stylesheet" href="https://fonts.googleapis.com/css2?family=PT+Sans:wght@400;700&family=PT+Serif&display=swap">
<style>
:root{
  --blue:#0a5c9c;
  --blue-dark:#06416f;
  --blue-text:#0d5aa0;
  --link:#1a73c0;
  --grey-text:#5a5a5a;
  --placeholder:#bdbdbd;
  --panel:#ffffff;
  --sky:#e7f4f9;
  --footer-blue:#0c4f95;
  --red:#c8161d;
  --coat:#dfe5ea;
  --coat-light:#eef2f5;
  --skin:#e9c7a8;
}
*{margin:0;padding:0;box-sizing:border-box}
html,body{width:1015px;height:1200px;overflow:hidden}
body{position:relative;font-family:"PT Sans",Arial,sans-serif;color:var(--grey-text);
  background:linear-gradient(to bottom,#f2f9fc 0,#ffffff 40px,#ffffff 165px,var(--sky) 220px,#eaf6fa 1020px,var(--footer-blue) 1021px,#083f7c 1200px)}
.abs{position:absolute}
.header-band{left:0;top:40px;width:1015px;height:126px;background:#fff}
.brand{left:74px;top:34px;display:flex;align-items:center;gap:10px;font-size:42px;font-weight:700;color:var(--blue-text);letter-spacing:.5px}
.brand-mark{width:30px;height:30px;border-radius:50%;background:#1c8ad6}
.call{left:732px;top:58px;width:215px;font-family:"PT Serif",Georgia,serif}
.call-label{position:absolute;left:74px;top:0;font-size:18px;color:#6b6b6b}
.call-number{position:absolute;left:42px;top:21px;font-size:27px;color:var(--blue-dark);white-space:nowrap}
.call-icon{position:absolute;left:0;top:16px}
.nav{left:46px;top:125px;width:923px;height:38px;border-radius:6px 6px 0 0;
  background:linear-gradient(#1f86c4,#0a5c9c 55%,#064c86);display:flex}
.nav a{color:#fff;text-decoration:none;font-size:13px;display:flex;align-items:center;justify-content:center;
  border-right:1px solid #3e8fc5;height:100%}
.nav a:last-child{border-right:0}
.panel{left:46px;top:163px;width:923px;height:953px;background:var(--panel);border-radius:0 0 8px 8px;box-shadow:0 3px 5px rgba(0,0,0,.15)}
.hero{left:65px;top:171px;width:886px;height:341px;
  background:
    linear-gradient(to bottom,rgba(255,255,255,0) 0,rgba(255,255,255,0) 12%,rgba(233,199,168,.55) 18%,rgba(233,199,168,.55) 30%,rgba(255,255,255,0) 38%),
    linear-gradient(to right,#f7f9fb 0,var(--coat) 12%,var(--coat-light) 24%,var(--coat) 38%,#d3dbe2 50%,var(--coat-light) 62%,var(--coat) 74%,var(--coat-light) 86%,#e2e8ee 97%,#f7f9fb 100%)}
.strip{left:64px;top:512px;width:887px;height:85px;border:1px solid #2a6fb3;border-radius:0 0 8px 8px;overflow:hidden;display:flex}
.strip div{height:100%}
h2{font-weight:400;color:var(--blue-text)}
.welcome-title{left:66px;top:622px;font-size:19px}
.welcome-text{left:65px;top:650px;width:648px;font-size:11.6px;line-height:18.4px;letter-spacing:.05px}
.login{left:728px;top:615px;width:223px;height:201px;border:1px solid #cfd6da;border-radius:4px;background:#fff;box-shadow:0 6px 6px -4px rgba(0,0,0,.2)}
.login-head{height:45px;background:#eef2f4;border-bottom:1px solid #d7dde0;display:flex;align-items:center;padding-left:15px;gap:8px;font-size:18px;color:var(--blue-text)}
.field{position:absolute;left:8px;font-size:11.5px;color:#666}
.field span{display:inline-block;width:62px}
.field i{position:absolute;left:68px;top:-4px;width:142px;height:21px;border:1px solid #c9c9c9;background:#fff}
.login-btn{position:absolute;left:131px;top:130px;width:82px;height:22px;border-radius:3px;background:linear-gradient(#1f74c9,#0b4ea3);color:#fff;font-size:11px;font-weight:700;display:flex;align-items:center;justify-content:center}
.login-links{position:absolute;left:0;width:100%;top:168px;text-align:center;font-size:10.5px;color:#666}
.feature{top:808px;width:196px}
.feature h2{font-size:18px;margin-bottom:10px}
.feature .thumb{width:195px;height:97px;border:1px solid #cfcfcf;padding:3px;background:#fff}
.feature .thumb div{width:100%;height:100%;background:var(--placeholder)}
.feature p{margin-top:10px;font-size:11.3px;line-height:14.8px;text-align:justify}
.more{position:absolute;font-size:11px;color:var(--link)}
.news-title{left:742px;top:834px;font-size:18px}
.news-rule{left:731px;top:860px;width:218px;height:1px;background:#d4d4d4}
.news-item{left:736px;width:215px;display:flex;gap:10px}
.news-item .thumb{width:59px;height:40px;background:var(--placeholder);flex:none}
.news-item p{font-size:10px;line-height:14px}
.community{left:46px;top:1043px;width:923px;height:64px;background:linear-gradient(#f4f4f4,#e3e5e7);display:flex;align-items:center}
.community-title{margin-left:12px;width:283px;font-size:15.5px;color:#444;letter-spacing:.3px}
.social{display:flex;align-items:center;gap:8px;font-size:14px;color:#444;line-height:16px}
.social b{font-weight:400;font-size:15.5px}
.social-sq{width:39px;height:39px;border-radius:5px;flex:none}
.footer-nav{left:148px;top:1134px;width:748px;display:flex;justify-content:space-between;font-size:11.5px;color:#fff}
.copyright{left:0;top:1168px;width:1015px;text-align:center;font-size:11.5px;color:#fff}
</style>
</head>
<body>
<div class="abs header-band"></div>

<div class="abs brand"><span class="brand-mark"></span>Medvista</div>

<div class="abs call">
  <svg class="call-icon" width="30" height="36" viewBox="0 0 30 36">
    <path d="M6 3c-3 2-4 6-3 11 2 8 8 16 15 19 3 1 6 1 8-1l-5-7-4 2c-3-2-6-7-6-11l3-3z" fill="var(--red)"/>
  </svg>
  <span class="call-label">Call Us</span>
  <span class="call-number">1800-555-0142</span>
</div>

<nav class="abs nav">
  <a style="width:91px">Home</a>
  <a style="width:102px">About Us</a>
  <a style="width:102px">VIP Club</a>
  <a style="width:98px">Services</a>
  <a style="width:170px">Packages and Prices</a>
  <a style="width:146px">Registration</a>
  <a style="width:127px">Testimonials</a>
  <a style="width:87px">Contacts</a>
</nav>

<div class="abs panel"></div>

<div class="abs hero" role="img" aria-label="Photo of a team of five smiling doctors in white coats with stethoscopes and clipboards"></div>

<div class="abs strip">
  <div role="img" aria-label="Red hospital emergency sign" style="width:178px;background:linear-gradient(90deg,#4a0606,#9e1418 40%,#c72a2a 70%,#7a0e10)"></div>
  <div role="img" aria-label="Airplane flying above clouds at sunset" style="width:179px;background:linear-gradient(#6b4a2a,#f0b24a 35%,#e59a3a 55%,#8a5a35 80%,#4a3528)"></div>
  <div role="img" aria-label="Clinic reception desk" style="width:176px;background:linear-gradient(90deg,#3a332d,#8a7258 40%,#c8b08a 60%,#4a3e35)"></div>
  <div role="img" aria-label="Group of doctors" style="width:178px;background:linear-gradient(#ffffff,#dfe5ea 50%,#eef1f4)"></div>
  <div role="img" aria-label="Smiling consultant" style="width:176px;background:linear-gradient(90deg,#ffffff 20%,#e9c7a8 55%,#b08d6a 70%,#ffffff 90%)"></div>
</div>

<h2 class="abs welcome-title">Welcome to our site</h2>
<p class="abs welcome-text">Lorem ipsum dolor sit amet, consectetuer adipiscing elit. Aenean commodo ligula eget dolor. Aenean massa. Cum sociis natoque penatibus et magnis dis parturient montes, nascetur ridiculus mus.Lorem ipsum dolor sit amet, consectetuer adipiscing elit. Aenean commodo ligula eget dolor. Aenean massa. Cum sociis natoque penatibus et magnis dis parturient montes, nascetur ridiculus mus.Lorem ipsum dolor sit amet, consectetuer adipiscing elit. Aenean commodo ligula eget dolor. Aenean massa. Cum sociis natoque penatibus et magnis dis parturient montes, nascetur ridiculus mus.Lorem ipsum dolor sit amet, consectetuer adipiscing elit. Aenean commodo ligula eget dolor. Aenean massa. Cum sociis natoque penatibus et magnis dis parturient montes, nascetur ridiculus mus.</p>

<div class="abs login">
  <div class="login-head">Login
    <svg width="20" height="26" viewBox="0 0 20 26"><path d="M5 11V7a5 5 0 0 1 10 0v4" fill="none" stroke="#777" stroke-width="2.5"/><circle cx="10" cy="17" r="8" fill="#2a6fb3" stroke="#555" stroke-width="1.5"/><circle cx="10" cy="17" r="3" fill="#cfe3f5"/></svg>
  </div>
  <div class="field" style="top:68px"><span>Username :</span><i></i></div>
  <div class="field" style="top:107px"><span>Password &nbsp;:</span><i></i></div>
  <div class="login-btn">LOGIN</div>
  <div class="login-links">Forgot password ? &nbsp;/&nbsp; Create new</div>
</div>

<div class="abs feature" style="left:66px">
  <h2>Lorem ipsum dolor sit</h2>
  <div class="thumb"><div role="img" aria-label="Feature image"></div></div>
  <p>Lorem ipsum dolor sit amet, consectetuer adipiscing elit. Aenean commodo ligula eget dolor. Aenean massa. Cum sociis natoque penatibus et magnis dis parturien</p>
</div>
<div class="abs feature" style="left:293px">
  <h2>Lorem ipsum dolor sit</h2>
  <div class="thumb"><div role="img" aria-label="Feature image"></div></div>
  <p>Lorem ipsum dolor sit amet, consectetuer adipiscing elit. Aenean commodo ligula eget dolor. Aenean massa. Cum sociis natoque penatibus et magnis dis parturien</p>
</div>
<div class="abs feature" style="left:523px">
  <h2>Lorem ipsum dolor sit</h2>
  <div class="thumb"><div role="img" aria-label="Feature image"></div></div>
  <p>Lorem ipsum dolor sit amet, consectetuer adipiscing elit. Aenean commodo ligula eget dolor. Aenean massa. Cum sociis natoque penatibus et magnis dis parturien</p>
</div>
<span class="more" style="left:200px;top:1019px">more &nbsp;››</span>
<span class="more" style="left:432px;top:1019px">more &nbsp;››</span>
<span class="more" style="left:663px;top:1019px">more &nbsp;››</span>

<h2 class="abs news-title">Latest News</h2>
<div class="abs news-rule"></div>
<div class="abs news-item" style="top:871px"><div class="thumb" role="img" aria-label="News image"></div><p>Lorem ipsum dolor sit amecon-sectetuer adipiscing elit</p></div>
<div class="abs news-item" style="top:918px"><div class="thumb" role="img" aria-label="News image"></div><p>Lorem ipsum dolor sit amecon-sectetuer adipiscing elit</p></div>
<div class="abs news-item" style="top:965px"><div class="thumb" role="img" aria-label="News image"></div><p>Lorem ipsum dolor sit amecon-sectetuer adipiscing elit</p></div>
<span class="more" style="left:901px;top:1018px">more &nbsp;››</span>

<div class="abs community">
  <div class="community-title">JOIN OUR ONLINE COMMUNITY...</div>
  <div class="social" style="width:154px"><span class="social-sq" style="background:#3b5a9a"></span><span>Join us on<br><b>Circlebook</b></span></div>
  <div class="social" style="width:156px"><span class="social-sq" style="background:#56b7d6"></span><span>Follow us on<br><b>Chirper</b></span></div>
  <div class="social" style="width:126px"><span class="social-sq" style="background:#e8641c"></span><span>Visit our<br><b>Blog</b></span></div>
  <div class="social"><span class="social-sq" style="background:#0b6aa5"></span><span>Connect with us on<br><b>Linkpro</b></span></div>
</div>

<div class="abs footer-nav">
  <span>Home</span><span>|</span><span>About Us</span><span>|</span><span>VIP Club</span><span>|</span><span>Services</span><span>|</span><span>Packages and Prices</span><span>|</span><span>Registration</span><span>|</span><span>Testimonials</span><span>|</span><span>Contacts</span>
</div>
<div class="abs copyright">© Copyright 2009 - 2010. Your Site Name Dot Com. All Rights Reserved</div>
</body>
</html>
```